Business cards for a naturopathic day clinic for stem cell therapy

We need a basic design for a day clinic, that offers stem cell therapies for Lyme therapy and other severe chronic illnesses.
Our name is "Haus solvaKrĂ¤ut", which can be translated into "Manor solvaHerb". We are a couple of naturopaths working along side physiotherapists and osteopaths, yoga teachers and massage therapists. I attached our logo.

```html
<!DOCTYPE html>
<html lang="en">
<head>
<meta charset="utf-8">
<title>Haus solvaKräut – Business Cards</title>
<link rel="stylesheet" href="https://fonts.googleapis.com/css2?family=Montserrat:wght@800&family=Arimo:wght@400&display=swap">
<style>
  :root {
    --page-bg: #ececec;
    --brand-green: #bbc46a;
    --card-white: #ffffff;
    --text-taupe: #8a7d72;
    --card-shadow: rgba(0, 0, 0, 0.12);
  }
  * { margin: 0; padding: 0; box-sizing: border-box; }
  html, body {
    width: 1200px;
    height: 1200px;
    overflow: hidden;
    background: var(--page-bg);
  }
  .sheet {
    position: relative;
    width: 1200px;
    height: 1200px;
  }
  .card {
    position: absolute;
    left: 250px;
    width: 700px;
    height: 400px;
    box-shadow: 0 6px 22px var(--card-shadow);
  }

  /* Front side */
  .card--front {
    top: 150px;
    background: var(--brand-green);
    display: flex;
    align-items: center;
    justify-content: center;
    gap: 22px;
  }
  .brand-dot {
    width: 46px;
    height: 46px;
    border-radius: 50%;
    background: var(--card-white);
  }
  .brand-name {
    font-family: "Arimo", Arial, sans-serif;
    font-weight: 400;
    letter-spacing: 1px;
  }
  .card--front .brand-name {
    color: var(--card-white);
    font-size: 54px;
  }

  /* Back side */
  .card--back {
    top: 650px;
    background: var(--card-white);
    font-family: "Arimo", Arial, sans-serif;
  }
  .holder-name {
    position: absolute;
    left: 68px;
    top: 78px;
    font-family: "Montserrat", Arial, sans-serif;
    font-weight: 800;
    font-size: 38px;
    letter-spacing: 5px;
    color: var(--brand-green);
  }
  .holder-role {
    position: absolute;
    left: 70px;
    top: 132px;
    font-size: 17px;
    letter-spacing: 6px;
    color: var(--text-taupe);
  }
  .contact-list {
    position: absolute;
    left: 76px;
    top: 176px;
    list-style: none;
  }
  .contact-item {
    display: flex;
    align-items: center;
    gap: 14px;
    height: 40px;
    font-size: 17px;
    letter-spacing: 4px;
    color: var(--text-taupe);
  }
  .contact-icon {
    width: 20px;
    height: 20px;
    flex: none;
  }
  .address {
    position: absolute;
    left: 78px;
    top: 316px;
    font-size: 11px;
    line-height: 20px;
    letter-spacing: 2px;
    color: var(--brand-green);
  }
  .card-brand {
    position: absolute;
    right: 48px;
    bottom: 62px;
    display: flex;
    align-items: center;
    gap: 10px;
  }
  .card-brand .brand-dot {
    width: 22px;
    height: 22px;
    background: var(--brand-green);
  }
  .card-brand .brand-name {
    font-size: 22px;
    color: var(--brand-green);
  }
</style>
</head>
<body>
<main class="sheet">

  <section class="card card--front" aria-label="Card front">
    <span class="brand-dot"></span>
    <span class="brand-name">Haus solvaKräut</span>
  </section>

  <section class="card card--back" aria-label="Card back">
    <h1 class="holder-name">YOUR NAME</h1>
    <p class="holder-role">POSITION</p>

    <ul class="contact-list">
      <li class="contact-item">
        <svg class="contact-icon" viewBox="0 0 24 24" aria-hidden="true">
          <path fill="#8a7d72" d="M6.6 10.8a15.1 15.1 0 0 0 6.6 6.6l2.2-2.2a1 1 0 0 1 1-.25 11.4 11.4 0 0 0 3.6.57 1 1 0 0 1 1 1V20a1 1 0 0 1-1 1A17 17 0 0 1 3 4a1 1 0 0 1 1-1h3.5a1 1 0 0 1 1 1c0 1.25.2 2.45.57 3.57a1 1 0 0 1-.25 1z"/>
        </svg>
        +00-0000-0000-000
      </li>
      <li class="contact-item">
        <svg class="contact-icon" viewBox="0 0 24 24" aria-hidden="true">
          <rect x="2.5" y="5" width="19" height="14" fill="none" stroke="#8a7d72" stroke-width="1.8"/>
          <path d="M2.5 5l9.5 8 9.5-8" fill="none" stroke="#8a7d72" stroke-width="1.8"/>
        </svg>
        INFO@COMPANYNAME.COM
      </li>
      <li class="contact-item">
        <svg class="contact-icon" viewBox="0 0 24 24" aria-hidden="true">
          <g fill="none" stroke="#8a7d72" stroke-width="1.8">
            <circle cx="12" cy="12" r="9.5"/>
            <ellipse cx="12" cy="12" rx="4.2" ry="9.5"/>
            <path d="M2.5 12h19M4 7h16M4 17h16"/>
          </g>
        </svg>
        WWW.COMPANYNAME.COM
      </li>
    </ul>

    <address class="address">
      1234 YOUR LOCATION HERE<br>
      YOUR RD. YOUR STREET<br>
      POSTAL 0000
    </address>

    <div class="card-brand">
      <span class="brand-dot"></span>
      <span class="brand-name">Haus solvaKräut</span>
    </div>
  </section>

</main>
</body>
</html>
```